BRIGHT COLORFUL + 55 FAMILY HISTORY BROCHURE 11 x 17 bifold

11 x 17 Bifold Flyer I have given you the Layout I just need you to make it Pretty

YOU DO NOT NEED TO FOLLOW MY LAYOUT, You can but dont have too

Target Market(s)

55 year old consumers, who could choose our service of Hereditary Cancer Screening

Industry/Entity Type

Health And Wellness

Requirements
Must have
• Must be appealing to Grand Parents, must make them want to test , show lots of pictures of grand children, YOU DO NOT NEED TO FOLLOW MY LAYOUT , You can but dont have too
Nice to have
• use our colors of our logo , YOU DO NOT NEED TO FOLLOW MY LAYOUT , You can but dont have too
Should not have
• YOU DO NOT NEED TO FOLLOW MY LAYOUT, You can but dont have too

```html
<!DOCTYPE html>
<html lang="en">
<head>
<meta charset="utf-8">
<title>Hereditary Cancer Screening – Bifold Brochure</title>
<link href="https://fonts.googleapis.com/css2?family=Libre+Baskerville:ital,wght@0,400;0,700;1,400&family=Crimson+Text:ital,wght@0,400;0,600;0,700;1,400&display=swap" rel="stylesheet">
<style>
:root{
  --navy:#1c2a6b;
  --navy-deep:#141f55;
  --green:#8cc63f;
  --green-dark:#6ea82a;
  --paper:#ffffff;
  --mist:#e9eaee;
  --ink:#2a2f45;
  --backdrop:#e4e4e4;
  --photo-warm:#c9b39d;
  --photo-soft:#d9cfc4;
  --photo-garden:#7f9a5a;
  --photo-leaf:#a7c46a;
}
*{margin:0;padding:0;box-sizing:border-box}
html,body{width:1200px;height:3333px;overflow:hidden;background:var(--backdrop)}
body{position:relative;font-family:"Crimson Text",Georgia,serif;color:var(--ink)}
.spread{position:absolute;left:78px;width:1044px;background:var(--paper);box-shadow:0 4px 14px rgba(0,0,0,.22);overflow:hidden}
.spread--outside{top:18px;height:838px}
.spread--inside{top:1662px;height:890px}
.panel{position:absolute;top:0;width:522px;height:100%}
.panel--left{left:0}
.panel--right{left:522px}
.panel svg.shapes{position:absolute;inset:0;width:100%;height:100%}
.txt{position:absolute}
.cover-kicker{top:36px;left:10px;right:10px;text-align:center;color:#fff;font-family:"Libre Baskerville",Georgia,serif;font-size:16.5px;line-height:1.6}
.decision{top:432px;left:30px;width:470px;color:var(--navy);font-family:"Libre Baskerville",Georgia,serif;font-size:17px;line-height:1.4}
.intro{top:560px;left:36px;width:450px;text-align:center;font-size:16.5px;line-height:1.45;color:var(--ink)}
.brand{display:flex;align-items:center;gap:8px;color:var(--navy);font-family:"Libre Baskerville",Georgia,serif;font-weight:700;font-size:15px;line-height:1.1}
.brand-dot{width:26px;height:26px;border-radius:50%;background:var(--green);flex:none}
.url{font-size:13px;color:var(--navy);font-weight:600}
.title{top:34px;left:14px;color:var(--navy);font-family:"Libre Baskerville",Georgia,serif;font-weight:700;font-size:37px;line-height:1.05}
.tagline{top:122px;left:60px;color:var(--green);font-family:"Libre Baskerville",Georgia,serif;font-style:italic;font-size:14px}
.gift-question{top:600px;right:22px;text-align:right;color:var(--navy);font-family:"Libre Baskerville",Georgia,serif;font-size:16px;line-height:1.3}
.gift-line{top:698px;right:22px;color:var(--green-dark);font-family:"Libre Baskerville",Georgia,serif;font-weight:700;font-size:17px}
.power-line{top:736px;right:22px;color:var(--navy);font-family:"Libre Baskerville",Georgia,serif;font-size:13.5px}
.power-line b{font-weight:700}
.stories{top:20px;left:20px;width:482px;font-size:12.5px;line-height:1.4;font-style:italic;color:var(--ink)}
.stories p{margin-bottom:22px}
.stories p.indent{padding-left:90px}
.positive{top:512px;left:210px;width:178px;color:var(--green);font-family:"Libre Baskerville",Georgia,serif;font-weight:700;font-size:18px;line-height:1.32}
.difference{top:764px;left:112px;width:390px;color:var(--navy);font-family:"Libre Baskerville",Georgia,serif;font-weight:700;font-size:16.5px;line-height:1.3}
.risk-head{top:432px;right:22px;text-align:right;color:var(--green-dark);font-family:"Libre Baskerville",Georgia,serif;font-weight:700;font-size:18.5px;line-height:1.28}
.risk-head span{color:var(--green)}
.facts{top:566px;left:22px;width:482px;font-size:11px;line-height:1.36;color:var(--ink)}
.facts p{margin-bottom:8px}
.facts em{color:var(--green-dark);font-style:italic}
</style>
</head>
<body>

<!-- Outside spread -->
<section class="spread spread--outside">
  <div class="panel panel--left">
    <svg class="shapes" viewBox="0 0 522 838" preserveAspectRatio="none">
      <rect width="522" height="838" fill="var(--paper)"/>
      <path d="M0 0H522V190Q300 150 0 205Z" fill="var(--navy)"/>
      <path d="M60 150Q300 110 522 145V360Q330 330 140 420Q90 400 60 380Z" fill="var(--mist)"/>
    </svg>
    <svg class="shapes" viewBox="0 0 522 838" preserveAspectRatio="none" role="img" aria-label="Photo of smiling grandparents with their grandchildren">
      <defs><linearGradient id="g1" x1="0" x2="1"><stop offset="0" stop-color="var(--photo-soft)"/><stop offset="1" stop-color="var(--photo-warm)"/></linearGradient></defs>
      <path d="M80 160Q300 125 500 158V345Q330 325 150 400Q100 385 80 365Z" fill="url(#g1)"/>
    </svg>
    <div class="txt cover-kicker">DOES CANCER Run in Your Family?<br>A Simple Swab Could SAVE a Family Members LIFE</div>
    <div class="txt decision">Your decision won't<br>just affect you. It will also impact Your Family, since your test results may Forecast Their Cancer Risks, too.</div>
    <div class="txt intro">We believe it is important to understand what can and cannot be learned with genetic testing. Genetic mutations can increase risks for certain cancers, but this does not mean cancer will definitely develop. You should be prepared to receive positive or negative results. Most people receive Negative Results meaning no mutations associated with an increased risk for the Hereditary cancers.</div>
    <div class="txt brand" style="top:772px;left:30px"><span class="brand-dot"></span><span>KINWELL<br>HEALTH GROUP</span></div>
    <div class="txt url" style="top:790px;right:24px">www.kinwellscreening.com</div>
  </div>

  <div class="panel panel--right">
    <svg class="shapes" viewBox="0 0 522 838" preserveAspectRatio="none">
      <rect width="522" height="838" fill="var(--paper)"/>
      <path d="M0 570Q260 530 522 560V760H0Z" fill="var(--mist)"/>
    </svg>
    <svg class="shapes" viewBox="0 0 522 838" preserveAspectRatio="none" role="img" aria-label="Green-tinted photo of a grandmother hugging a grandchild">
      <defs><linearGradient id="g2" x1="0" x2="1"><stop offset="0" stop-color="var(--photo-leaf)"/><stop offset="1" stop-color="var(--green-dark)"/></linearGradient></defs>
      <path d="M290 0H522V300Q400 200 290 0Z" fill="url(#g2)"/>
    </svg>
    <svg class="shapes" viewBox="0 0 522 838" preserveAspectRatio="none" role="img" aria-label="Photo of a three-generation family smiling together">
      <path d="M0 190Q120 170 300 150Q420 250 522 300V560Q260 520 0 585Z" fill="url(#g1)"/>
    </svg>
    <div class="txt title">Hereditary Cancer<br>Screening</div>
    <div class="txt tagline">"The Test You Take For Them"</div>
    <div class="txt gift-question">Will You give<br>Your loved ones the<br>information to Beat Cancer<br>in their lives ?</div>
    <div class="txt gift-line">Give Them the Gift of Knowledge</div>
    <div class="txt power-line">Knowing is better than not knowing. <b>Knowledge is Power</b></div>
    <div class="txt brand" style="top:772px;left:24px"><span class="brand-dot"></span><span>KINWELL<br>HEALTH GROUP</span></div>
    <div class="txt url" style="top:790px;right:24px">www.kinwellscreening.com</div>
  </div>
</section>

<!-- Inside spread -->
<section class="spread spread--inside">
  <div class="panel panel--left">
    <svg class="shapes" viewBox="0 0 522 890" preserveAspectRatio="none">
      <rect width="522" height="890" fill="var(--paper)"/>
      <path d="M0 500Q90 470 200 480V760Q100 765 0 800Z" fill="var(--navy)"/>
      <path d="M0 840Q260 825 522 815V890H0Z" fill="var(--green)"/>
    </svg>
    <svg class="shapes" viewBox="0 0 522 890" preserveAspectRatio="none" role="img" aria-label="Photo of a grandmother and granddaughter smiling cheek to cheek">
      <path d="M0 540Q100 505 190 520Q210 640 180 750Q90 760 0 790Z" fill="url(#g1)"/>
    </svg>
    <div class="txt stories">
      <p>Genetic testing revealed Daniel Marsh carried a mutation that gave him a 55 to 70 percent chance of developing stomach cancer. Early screening revealed there were 14 sites of stage 1A cancer. Once the news sank in, he realized his Mother's Genetic Testing Saved His Life.</p>
      <p class="indent">Genetic Testing Saved My Life. Because of my age and family background, my doctor recommended Genetic Testing and they were right. I had a gene change, because of this my other two sisters got tested. My younger sister was positive and my older sister was negative. Now we can take steps to lower the risks, including enhanced screening and preventive care.</p>
      <p>A breast cancer survivor before age 50: "Genetic testing saved my life" Carla Reyes was diagnosed with breast cancer two weeks before her 40th birthday. Now cancer free, she credits her recovery to awareness of a hereditary mutation that predisposed her and her family to the disease. After my mom tested positive, I chose testing and was referred to a clinic for increased surveillance. My medical care providers were very diligent in making sure I was watched closely. Knowledge is power and, in this case, Genetic testing saved my life!</p>
      <p class="indent">My father had genetic testing and found he had a hereditary colorectal cancer syndrome. My name is Helen Ward and I am a 27 year survivor of colorectal cancer. From an early age I learned the importance of screenings and knew the signs and symptoms. Following screening guidelines for individuals at an increased risk &amp; knowing my family history saved my life!</p>
    </div>
    <div class="txt positive">A Positive result or finding a mutation is Not a Cancer Diagnosis and does not mean you will ever develop Cancer</div>
    <div class="txt difference">learning if you have an increased risk for cancer can make a difference</div>
    <div class="txt url" style="top:858px;left:24px;color:#fff">www.kinwellscreening.com</div>
  </div>

  <div class="panel panel--right">
    <svg class="shapes" viewBox="0 0 522 890" preserveAspectRatio="none">
      <rect width="522" height="890" fill="var(--paper)"/>
      <path d="M300 890Q420 850 522 828V890Z" fill="var(--navy)"/>
    </svg>
    <svg class="shapes" viewBox="0 0 522 890" preserveAspectRatio="none" role="img" aria-label="Photo of grandparents playing with young grandchildren in a garden">
      <defs><linearGradient id="g3" x1="0" x2="1" y1="0" y2="1"><stop offset="0" stop-color="var(--photo-leaf)"/><stop offset=".6" stop-color="var(--photo-garden)"/><stop offset="1" stop-color="var(--photo-warm)"/></linearGradient></defs>
      <path d="M40 180Q200 40 522 0V425Q380 410 300 430Q140 395 40 180Z" fill="url(#g3)"/>
    </svg>
    <div class="txt risk-head">There are<br>many Known<br>risk factors for Cancer.<br><span>GENETICS and FAMILY HISTORY<br>are Often Overlooked.</span></div>
    <div class="txt facts">
      <p>Genetic Testing is done to determine whether family members without obvious illness have inherited the same mutation as a family member who is known to carry a cancer associated mutation. Meaning Will You Help Your Kids &amp; Grand Children.</p>
      <p><b>What are the benefits of testing?</b> <em>"The Power of Knowledge"</em> <b>Helping Younger Family Members Know if there is a Risk and Preparing for it.</b> Knowing if you have a genetic mutation lets you work with your doctor to monitor and address your cancer risks. According to the National Cancer Council eating 5 or more servings of vegetables &amp; fruit, and limiting red meat, dairy and eggs will help prevent or delay cancer.</p>
      <p>There are many benefits to getting tested, regardless of the eventual result. If one of your family members — however distant — had cancer, there is a chance that you inherited a gene mutation that not only increases your personal risk of cancer, but also could be passed to the next generation. Those who are carriers of hereditary cancer gene mutations could be at risk of getting cancer earlier in life than the general population. The sooner genetic testing is done, the more likely it is that the risk can be managed appropriately.</p>
    </div>
    <div class="txt url" style="top:862px;right:22px;color:#fff">www.kinwellscreening.com</div>
  </div>
</section>

</body>
</html>
```